Boring Fiberglass Repair Company needs creative business cards

The Fiberglass Repair industry isn't very fun or creative but we'd like a business card that communicates a fresh, modern, and service-oriented feel. We repair bathroom fixtures (bath tubs, showers, etc) which are made out of fiberglass. Our fiberglass repair service will be sold to bathtub manufacturers and also businesses that sell bathtubs. We will also offer our services to home owners that have broken showers and bathtubs.
Target Market(s)
Home builders, plumbing wholesalers, home owners
Contact Information for Business Card
Name
Phone Number
Email Address
Business Address
Tag line: "Quality Craftsmanship Today"

```html
<!DOCTYPE html>
<html lang="en">
<head>
<meta charset="utf-8">
<title>Mesa Ridge Fiberglass – Business Cards</title>
<link href="https://fonts.googleapis.com/css2?family=Arimo:wght@400;700&display=swap" rel="stylesheet">
<style>
  :root {
    --navy: #1c2a5c;
    --red: #e3232c;
    --ink: #4a4a4a;
    --rule: #c9ccd8;
    --paper: #ffffff;
    --backdrop: #e9e6e1;
  }
  * { box-sizing: border-box; margin: 0; padding: 0; }
  html, body { width: 1200px; height: 900px; overflow: hidden; }
  body {
    background: var(--backdrop);
    font-family: "Arimo", Arial, sans-serif;
    position: relative;
  }
  .card {
    position: absolute;
    left: 250px;
    width: 700px;
    height: 400px;
    background: var(--paper);
    box-shadow: 0 10px 30px rgba(0,0,0,0.18);
    display: flex;
    flex-direction: column;
    align-items: center;
  }
  .card--front { top: 35px; border: 10px solid var(--red); justify-content: center; }
  .card--back { top: 465px; border: 10px solid var(--navy); padding-top: 70px; }

  .wordmark {
    font-family: "Arimo", Arial, sans-serif;
    font-weight: 700;
    color: var(--navy);
    font-size: 46px;
    letter-spacing: 1px;
    text-transform: uppercase;
    line-height: 1;
  }
  .card--back .wordmark { font-size: 42px; }

  .person {
    display: flex;
    align-items: center;
    width: 580px;
    margin-top: 40px;
    gap: 14px;
  }
  .person__rule { flex: 1; height: 1px; background: linear-gradient(90deg, transparent, var(--rule)); }
  .person__rule--right { background: linear-gradient(90deg, var(--rule), transparent); }
  .person__text { text-align: center; }
  .person__name { font-weight: 700; color: var(--navy); font-size: 24px; letter-spacing: 0.5px; }
  .person__title { color: var(--ink); font-size: 17px; margin-top: 2px; }

  .contact { margin-top: 52px; text-align: center; color: var(--ink); font-size: 19px; line-height: 1.6; }
  .contact__line { display: flex; align-items: center; justify-content: center; gap: 8px; }
  .contact__sep { margin: 0 6px; }
  .icon { width: 18px; height: 18px; fill: var(--red); flex: none; }
</style>
</head>
<body>
  <section class="card card--front" aria-label="Business card front">
    <p class="wordmark">Mesa Ridge Fiberglass</p>
  </section>

  <section class="card card--back" aria-label="Business card back">
    <p class="wordmark">Mesa Ridge Fiberglass</p>

    <div class="person">
      <span class="person__rule"></span>
      <div class="person__text">
        <p class="person__name">JOHN DOE</p>
        <p class="person__title">Director</p>
      </div>
      <span class="person__rule person__rule--right"></span>
    </div>

    <div class="contact">
      <p class="contact__line">
        <svg class="icon" viewBox="0 0 24 24" aria-hidden="true"><path d="M3 8c0-3 4-5 9-5s9 2 9 5v2h-5V8c-1-1-7-1-8 0v2H3zM6 11h12l3 10H3z"/></svg>
        <span>1234 5678 90</span>
        <span class="contact__sep">|</span>
        <svg class="icon" viewBox="0 0 24 24" aria-hidden="true"><path d="M2 9l10-6 10 6v12H2zM4 10l8 5 8-5-8-5z"/></svg>
        <span>info@mesaridgefiberglass.com</span>
      </p>
      <p class="contact__line">
        <svg class="icon" viewBox="0 0 24 24" aria-hidden="true"><path d="M12 2a7 7 0 0 0-7 7c0 5 7 13 7 13s7-8 7-13a7 7 0 0 0-7-7zm0 10a3 3 0 1 1 0-6 3 3 0 0 1 0 6z"/></svg>
        <span>99 dummy city, dummy place, Dummy Land</span>
      </p>
    </div>
  </section>
</body>
</html>
```